We need an attractive business card design that is modern and inviting. We like the blue and yellow (or gold) colors that are displayed with the logo. The business should communicate trust, experience, and integrity.

Target Market(s)

Residential and Commercial

Industry/Entity Type

Business

Contact Information for Business Card

Recessed Lighting
LED Retro Fit
Sign Repair
Alarms and Cameras
Mobile Home Services
24hr service calls

Font styles to use
Serif
Sans Serif

Colors
3176b5
0455a3
fece3e
fbee3e

Requirements
Must have
• Brondle Electric
• Owner: Marcus Tivane
• Licensed and Insured
• TECL #58917
Nice to have
• Exquisite Detail!!
• Over 20 years of experience
Should not have
• Nothing boring or traditional!!!

```html
<!DOCTYPE html>
<html lang="en">
<head>
<meta charset="utf-8">
<title>Brondle Electric – Business Cards</title>
<link rel="stylesheet" href="https://fonts.googleapis.com/css2?family=Montserrat:wght@600;800&family=Quicksand:wght@400;500;600&display=swap">
<style>
  :root {
    --blue-deep: #2a2f9a;
    --blue-mid: #3b3fb0;
    --blue-brand: #0455a3;
    --blue-soft: #3176b5;
    --yellow: #fbee3e;
    --gold: #fece3e;
    --white: #ffffff;
    --backdrop: #e8e6e2;
  }
  * { box-sizing: border-box; margin: 0; padding: 0; }
  html, body { width: 1200px; height: 900px; overflow: hidden; }
  body {
    background: var(--backdrop);
    font-family: "Quicksand", sans-serif;
    position: relative;
  }
  .card {
    position: absolute;
    width: 700px;
    height: 400px;
    left: 250px;
    overflow: hidden;
    border-radius: 4px;
    box-shadow: 0 10px 30px rgba(0,0,0,0.18);
  }

  /* Front card */
  .card--front {
    top: 40px;
    background: radial-gradient(ellipse at 70% 40%, var(--blue-mid), var(--blue-deep) 75%);
    color: var(--white);
  }
  .front__decor-circle {
    position: absolute;
    left: -90px; top: 60px;
    width: 360px; height: 360px;
    border: 44px solid rgba(255,255,255,0.09);
    border-radius: 50%;
  }
  .front__decor-square {
    position: absolute;
    right: 0; top: 205px;
    width: 34px; height: 30px;
    background: rgba(255,255,255,0.14);
  }
  .front__brand {
    position: absolute;
    right: 40px; top: 58px;
    display: flex; align-items: center; gap: 14px;
  }
  .brand-dot {
    width: 46px; height: 46px;
    border: 5px solid var(--yellow);
    border-radius: 50%;
    flex: none;
  }
  .brand-name {
    font-family: "Montserrat", sans-serif;
    font-weight: 800;
    font-size: 24px;
    letter-spacing: 1.5px;
    color: var(--yellow);
    white-space: nowrap;
  }
  .front__tagline {
    position: absolute;
    right: 34px; top: 290px;
    font-size: 15px;
    font-weight: 500;
    letter-spacing: 0.4px;
    white-space: nowrap;
  }
  .front__tagline .divider { color: var(--gold); margin: 0 8px; }

  /* Back card */
  .card--back { top: 470px; background: var(--white); }
  .back__shapes { position: absolute; inset: 0; }
  .back__brand {
    position: absolute;
    left: 48px; top: 34px;
  }
  .back__brand .brand-dot {
    width: 128px; height: 128px;
    border: 10px solid var(--blue-brand);
    margin-left: 22px;
  }
  .back__brand .brand-name {
    color: var(--blue-brand);
    font-size: 25px;
    margin-top: 34px;
  }
  .back__license {
    position: absolute;
    left: 60px; top: 296px;
    color: var(--blue-soft);
    font-size: 17px;
    font-weight: 500;
    line-height: 1.3;
  }
  .services {
    position: absolute;
    right: 40px; top: 20px;
    color: var(--white);
    text-align: right;
  }
  .services__title {
    font-family: "Montserrat", sans-serif;
    font-weight: 600;
    font-size: 22px;
    letter-spacing: 2px;
    margin-bottom: 8px;
    margin-right: 70px;
  }
  .services__list { list-style: none; font-size: 15px; line-height: 1.22; font-weight: 500; }
  .owner {
    position: absolute;
    left: 440px; top: 238px;
    font-family: "Montserrat", sans-serif;
    font-weight: 600;
    font-size: 22px;
    letter-spacing: 2px;
    white-space: nowrap;
  }
  .owner__first { color: var(--blue-brand); }
  .owner__last { color: var(--yellow); }
  .contact {
    position: absolute;
    left: 440px;
    display: flex; align-items: center; gap: 10px;
    color: var(--white);
    font-size: 17px; font-weight: 500;
  }
  .contact--phone { top: 290px; }
  .contact--place { top: 330px; }
  .contact__icon { width: 22px; height: 22px; flex: none; }
</style>
</head>
<body>

  <section class="card card--front" aria-label="Business card front">
    <div class="front__decor-circle"></div>
    <div class="front__decor-square"></div>
    <div class="front__brand">
      <span class="brand-dot"></span>
      <span class="brand-name">BRONDLE ELECTRIC</span>
    </div>
    <p class="front__tagline">Exquisite Detail!!! <span class="divider">|</span> Over 20 years of experience</p>
  </section>

  <section class="card card--back" aria-label="Business card back">
    <svg class="back__shapes" viewBox="0 0 700 400" width="700" height="400" aria-hidden="true">
      <defs>
        <radialGradient id="back-blue" cx="70%" cy="40%" r="70%">
          <stop offset="0" stop-color="#3b3fb0"/>
          <stop offset="1" stop-color="#2a2f9a"/>
        </radialGradient>
      </defs>
      <polygon points="375,0 700,0 700,400 322,400 432,95 345,95" fill="url(#back-blue)"/>
      <polygon points="300,0 375,0 345,95 432,95 322,400 362,190 282,190" fill="#fbee3e"/>
    </svg>

    <div class="back__brand">
      <div class="brand-dot"></div>
      <div class="brand-name">BRONDLE ELECTRIC</div>
    </div>
    <p class="back__license">Licensed and Insured<br>TECL #58917</p>

    <div class="services">
      <h2 class="services__title">SERVICES</h2>
      <ul class="services__list">
        <li>Sign Repair</li>
        <li>LED Retro Fit</li>
        <li>24hr service calls</li>
        <li>Recessed Lighting</li>
        <li>Alarms and Cameras</li>
        <li>Mobile Home Services</li>
        <li>Residential and Commercial</li>
      </ul>
    </div>

    <p class="owner"><span class="owner__first">MARCUS</span> <span class="owner__last">TIVANE</span></p>

    <p class="contact contact--phone">
      <svg class="contact__icon" viewBox="0 0 22 22" aria-hidden="true">
        <circle cx="11" cy="11" r="11" fill="#fece3e"/>
        <rect x="7.5" y="5" width="7" height="12" rx="1.5" fill="none" stroke="#2a2f9a" stroke-width="1.6"/>
        <line x1="10" y1="14.5" x2="12" y2="14.5" stroke="#2a2f9a" stroke-width="1.4"/>
      </svg>
      936-555-0182
    </p>
    <p class="contact contact--place">
      <svg class="contact__icon" viewBox="0 0 22 22" aria-hidden="true">
        <circle cx="11" cy="11" r="11" fill="#fece3e"/>
        <path d="M11 17.5 C8 13.5 7 12 7 10 a4 4 0 0 1 8 0 c0 2-1 3.5-4 7.5z" fill="#2a2f9a"/>
        <circle cx="11" cy="10" r="1.5" fill="#fece3e"/>
      </svg>
      Harlow Creek, Texas
    </p>
  </section>

</body>
</html>
```